Quorvane Capital Modern Business Card

We need a modern business card template designed for Quorvane Capital.
Quorvane Capital is a diversified global cryptocurrency investment fund.

The font under the logo: Hiragino Kaku Gothic Pro

Color Hexcode: Main colors white (ffffff) & teal (188383), we are open to adding #fcca46 as an accent

Target Market(s)

Accredited Investors, high net worth individuals and institutional investors

Industry/Entity Type

Investment

Contact Information for Business Card

Contact Information should contain
Name
main phone +1 720 555 0147
cell
email

Font styles to use
Sans Serif
Other font styles liked:
• Hiragino Kaku Gothic Pro

Requirements
Must have
• would like to have icons that identify the contact information
• include our website: www.quorvanecapital.example
• include our Tagline: Diversified Crypto Investment Funds
Nice to have
• Would like to have a simple back side with the logo (without the words) and plenty of space

```html
<!DOCTYPE html>
<html lang="en">
<head>
<meta charset="utf-8">
<title>Quorvane Capital – Business Card</title>
<link rel="stylesheet" href="https://fonts.googleapis.com/css2?family=Noto+Sans+JP:wght@300;400;700&display=swap">
<style>
  :root {
    --backdrop: #3a322d;
    --card: #111111;
    --teal: #1f9a9a;
    --silver: #d6d6d6;
    --text-soft: #c9c9c9;
    --tagline: #9a9a9a;
    --divider: #3d3d3d;
  }
  * { box-sizing: border-box; margin: 0; padding: 0; }
  html, body {
    width: 1200px; height: 844px; overflow: hidden;
    background: var(--backdrop);
    font-family: "Noto Sans JP", "Helvetica Neue", Arial, sans-serif;
  }
  .stage {
    position: relative; width: 1200px; height: 844px;
    display: flex; align-items: center; justify-content: center; gap: 40px;
  }
  .card {
    width: 540px; height: 309px;
    background: var(--card);
    position: relative;
    box-shadow: 0 10px 30px rgba(0,0,0,.45);
  }
  /* Contact side */
  .card--contact { display: flex; }
  .brand-panel {
    width: 245px; display: flex; align-items: center; justify-content: center;
  }
  .brand-name {
    color: var(--teal); font-weight: 700; font-size: 20px;
    letter-spacing: .04em; text-align: center; line-height: 1.3;
  }
  .divider {
    width: 1px; margin: 60px 0; background: var(--divider);
  }
  .contact-panel {
    flex: 1; padding: 88px 0 0 34px;
  }
  .person-name {
    color: var(--teal); font-weight: 700; font-size: 19px;
    letter-spacing: .03em; margin-bottom: 12px;
  }
  .contact-list { list-style: none; }
  .contact-item {
    display: flex; align-items: center; gap: 10px;
    color: var(--text-soft); font-size: 15px; line-height: 22px;
  }
  .contact-icon { width: 12px; height: 12px; fill: var(--teal); flex: none; }
  /* Identity side */
  .card--identity {
    display: flex; flex-direction: column; align-items: center; justify-content: center;
  }
  .identity-name {
    color: var(--silver); font-weight: 300; font-size: 24px;
    letter-spacing: .08em; text-transform: uppercase; margin-bottom: 40px;
  }
  .tagline {
    color: var(--tagline); font-size: 13px; letter-spacing: .22em;
    text-transform: uppercase;
  }
</style>
</head>
<body>
<main class="stage">
  <section class="card card--contact">
    <div class="brand-panel">
      <p class="brand-name">Quorvane<br>Capital</p>
    </div>
    <div class="divider"></div>
    <div class="contact-panel">
      <h1 class="person-name">DANIEL OKAFOR</h1>
      <ul class="contact-list">
        <li class="contact-item">
          <svg class="contact-icon" viewBox="0 0 12 12"><path d="M2.5 1h2l1 2.7-1.3 1a6 6 0 0 0 2.8 2.8l1-1.3 2.7 1v2c0 .5-.5 1-1 1A9.8 9.8 0 0 1 1.5 2c0-.5.5-1 1-1z"/></svg>
          <span>+1 720 555 0147</span>
        </li>
        <li class="contact-item">
          <svg class="contact-icon" viewBox="0 0 12 12"><path d="M3.5 0h5a1 1 0 0 1 1 1v10a1 1 0 0 1-1 1h-5a1 1 0 0 1-1-1V1a1 1 0 0 1 1-1zm.3 1.5v7.5h4.4V1.5zM6 10a.6.6 0 1 0 0 1.2A.6.6 0 0 0 6 10z"/></svg>
          <span>044-555 019 284</span>
        </li>
        <li class="contact-item">
          <svg class="contact-icon" viewBox="0 0 12 12"><path d="M0 2.5h12v7H0zM.8 3.2 6 7l5.2-3.8v-.1H.8z"/></svg>
          <span>info@quorvane.example</span>
        </li>
        <li class="contact-item">
          <svg class="contact-icon" viewBox="0 0 12 12"><circle cx="6" cy="6" r="6"/><path d="M1 6h10M6 .5c2 2 2 9 0 11M6 .5c-2 2-2 9 0 11" stroke="#111" stroke-width=".8" fill="none"/></svg>
          <span>www.quorvanecapital.example</span>
        </li>
      </ul>
    </div>
  </section>

  <section class="card card--identity">
    <p class="identity-name">Quorvane Capital</p>
    <p class="tagline">Diversified Crypto Investment Funds</p>
  </section>
</main>
</body>
</html>
```